Business Card Design for company

We want new business cards. We'd like something different-- yet still highly professional. Our tagline is Providing leadership, delivering success. Stock photos are ok, as long as they are relevant and look upscale.

Target Market(s)

Architecture/Business Management Consulting/Engineering Consulting

Contact Information for Business Card

dark gray background with pops of blue might be good, but you tell me. You're the designers. Rounded corners might be nice, but again, you tell me.

Font styles to use
Serif
Sans Serif

Colors
3276b5
5c5c5c
9d9d9d
fbfbfb

Requirements
Nice to have
• Something different, but still very professional.

```html
<!DOCTYPE html>
<html lang="en">
<head>
<meta charset="utf-8">
<title>Halden Advisory – Business Card</title>
<link href="https://fonts.googleapis.com/css2?family=Lato:wght@400;700&family=Roboto:wght@400&display=swap" rel="stylesheet">
<style>
  :root {
    --backdrop: #2b2b2c;
    --card-white: #ffffff;
    --card-gray: #4a4d52;
    --brand-blue: #2e65a0;
    --rule-blue: #a9c0da;
    --text-gray: #4f4f52;
    --mark-gray: #55585d;
    --on-dark: #ffffff;
  }
  * { margin: 0; padding: 0; box-sizing: border-box; }
  html, body {
    width: 1125px; height: 1200px; overflow: hidden;
    background: var(--backdrop);
  }
  .canvas { position: relative; width: 1125px; height: 1200px; }

  .card { position: absolute; left: 150px; width: 825px; height: 471px; }
  .card-front { top: 98px; background: var(--card-white); font-family: "Lato", sans-serif; }
  .card-back { top: 631px; background: var(--card-gray); }

  .wordmark {
    position: absolute; right: 56px; top: 40px; text-align: right;
    color: var(--mark-gray); font-family: "Lato", sans-serif; font-weight: 700;
  }
  .wordmark-name { display: block; font-size: 70px; line-height: 1; letter-spacing: 1px; }
  .wordmark-sub { display: block; font-size: 27px; line-height: 1; letter-spacing: 2px; margin-top: 14px; }

  .person-name {
    position: absolute; left: 43px; top: 220px;
    color: var(--brand-blue); font-weight: 700; font-size: 30px; letter-spacing: 0.3px;
  }
  .person-title {
    position: absolute; left: 44px; top: 255px;
    color: var(--text-gray); font-weight: 700; font-size: 20px;
  }
  .contact-list { position: absolute; left: 45px; top: 292px; list-style: none; }
  .contact-item {
    display: flex; align-items: center; height: 27px;
    color: var(--text-gray); font-size: 20px;
  }
  .contact-icon { width: 20px; height: 18px; margin-right: 10px; fill: var(--brand-blue); }

  .address {
    position: absolute; right: 54px; top: 324px; text-align: right;
    color: var(--text-gray); font-size: 20px; line-height: 25px; font-style: normal;
  }
  .rule { position: absolute; left: 0; right: 0; top: 417px; height: 1px; background: var(--rule-blue); }
  .web-tab {
    position: absolute; left: 421px; top: 396px; width: 349px; height: 38px;
    background: var(--brand-blue); color: var(--on-dark);
    display: flex; align-items: center; justify-content: center;
    font-size: 19px; letter-spacing: 1.6px;
  }

  .back-wordmark {
    position: absolute; left: 0; right: 0; top: 172px; text-align: center;
    color: var(--on-dark); font-family: "Lato", sans-serif; font-weight: 700;
    font-size: 104px; line-height: 1; letter-spacing: 2px;
  }
  .tagline {
    position: absolute; left: 0; right: 0; top: 395px; text-align: center;
    color: var(--on-dark); font-family: "Roboto", sans-serif; font-size: 20px;
  }
  .tagline-dot {
    display: inline-block; width: 7px; height: 7px; border-radius: 50%;
    background: var(--on-dark); margin: 0 12px; vertical-align: middle;
  }
</style>
</head>
<body>
<main class="canvas">
  <section class="card card-front" aria-label="Card front">
    <div class="wordmark">
      <span class="wordmark-name">HALDEN</span>
      <span class="wordmark-sub">ADVISORY</span>
    </div>

    <h1 class="person-name">DANIEL REEVE</h1>
    <p class="person-title">CEO/FOUNDER</p>

    <ul class="contact-list">
      <li class="contact-item">
        <svg class="contact-icon" viewBox="0 0 24 24" aria-hidden="true"><path d="M6.6 10.8a15.2 15.2 0 0 0 6.6 6.6l2.2-2.2a1 1 0 0 1 1-.25 11.4 11.4 0 0 0 3.6.57 1 1 0 0 1 1 1V20a1 1 0 0 1-1 1A17 17 0 0 1 3 4a1 1 0 0 1 1-1h3.5a1 1 0 0 1 1 1c0 1.25.2 2.45.57 3.57a1 1 0 0 1-.25 1z"/></svg>
        <span>555 201 4837</span>
      </li>
      <li class="contact-item">
        <svg class="contact-icon" viewBox="0 0 24 24" aria-hidden="true"><path d="M7 2h10v5H7z M3 8h18a1 1 0 0 1 1 1v8h-4v-3H6v3H2V9a1 1 0 0 1 1-1z M7 15h10v7H7z"/></svg>
        <span>555 201 4838</span>
      </li>
      <li class="contact-item">
        <svg class="contact-icon" viewBox="0 0 24 24" aria-hidden="true"><path d="M2 6h20v13H2z M2 6l10 7 10-7" stroke="#ffffff" stroke-width="1.4"/></svg>
        <span>daniel@haldenadvisory.com</span>
      </li>
    </ul>

    <address class="address">1420 Alder Court<br>Anchorage, Alaska 99501</address>

    <div class="rule"></div>
    <div class="web-tab">www.haldenadvisory.com</div>
  </section>

  <section class="card card-back" aria-label="Card back">
    <div class="back-wordmark">HALDEN</div>
    <p class="tagline">Providing leadership<span class="tagline-dot"></span>delivering success</p>
  </section>
</main>
</body>
</html>
```